Webpage for balustrade importer and installer

We are a balustrade importer and installer. We sell a few different products mostly connected with glass and aluminum. We sell balconies, stairs, shower glass, mirrors, splash back glass, office partitions, glass dors and walls.

```html
<!DOCTYPE html>
<html lang="en">
<head>
<meta charset="utf-8">
<title>Norvale – Balustrade Importer and Installer</title>
<link href="https://fonts.googleapis.com/css2?family=Poppins:wght@300;400;500;600;800&family=Oswald:wght@300&display=swap" rel="stylesheet">
<style>
:root{
  --navy:#0f1e5a;
  --navy-deep:#0a1545;
  --blue:#1b3a9c;
  --blue-soft:#d4dcf0;
  --paper:#eef0f4;
  --ink:#1c1f2a;
  --muted:#4a4f5e;
  --white:#ffffff;
}
*{box-sizing:border-box;margin:0;padding:0}
html,body{width:1200px;height:3558px;overflow:hidden}
body{position:relative;font-family:'Poppins',sans-serif;color:var(--ink);background:var(--white)}
.abs{position:absolute}
.btn{position:absolute;display:flex;align-items:center;justify-content:center;gap:12px;background:var(--navy);color:var(--white);font-size:14px;font-weight:500;box-shadow:5px 5px 0 var(--blue-soft)}
/* hero */
.hero{left:0;top:0;width:1200px;height:612px;background:linear-gradient(180deg,#a9c1ec 0%,#c3d3ef 35%,#dfe2e8 60%,#cdd0d6 100%)}
.logo{font-family:'Oswald',sans-serif;font-weight:300;font-size:40px;letter-spacing:1px;color:var(--navy)}
.nav{top:58px;font-size:13px;color:var(--navy)}
.hero-title{left:87px;top:256px;font-size:55px;font-weight:800;color:var(--navy-deep)}
.hero-sub{left:87px;top:334px;font-size:20px;color:var(--navy-deep)}
/* headings */
.sec-title{font-size:29px;font-weight:800;color:var(--blue);line-height:1}
.sec-title span{background:linear-gradient(transparent 60%,var(--blue-soft) 60%);padding-right:6px}
.sec-sub{font-size:21px;color:var(--blue)}
.services{left:0;top:612px;width:1200px;height:617px;background:var(--paper)}
.tile{position:absolute}
.tile-label{position:absolute;left:14px;bottom:14px;height:48px;padding:0 28px;display:flex;align-items:center;background:var(--navy);color:var(--white);font-size:13px;font-weight:500}
.about-text{left:86px;top:1378px;width:674px;font-size:14px;line-height:21px;color:var(--ink)}
.about-text p+p{margin-top:14px}
.badge{position:absolute;width:116px;height:116px;border-radius:50%;background:#dfe4ef;display:flex;align-items:center;justify-content:center}
.badge::before{content:"";position:absolute;width:96px;height:96px;border-radius:50%;background:#c6d0e6}
.badge .core{position:relative;width:68px;height:68px;border-radius:50%;background:var(--blue);display:flex;align-items:center;justify-content:center}
.card{position:absolute;top:1864px;width:324px;height:181px;background:var(--white);box-shadow:0 4px 18px rgba(20,30,70,.09);display:flex;flex-direction:column;align-items:center;justify-content:center;text-align:center;padding:0 36px}
.card h3{font-size:17px;font-weight:500;color:var(--blue);margin-bottom:12px}
.card p{font-size:14px;line-height:22px;color:var(--ink)}
.stats{left:0;top:2541px;width:1200px;height:225px;background:linear-gradient(180deg,#ffffff 0%,#dfe3ec 100%)}
.stat{position:absolute;top:2622px;display:flex;align-items:center;gap:18px}
.stat b{display:block;font-size:20px;font-weight:400;color:var(--navy)}
.stat small{font-size:14px;color:var(--muted)}
.world{left:0;top:2766px;width:1200px;height:792px;background:linear-gradient(180deg,#0a1543 0%,#0f1e5a 40%,#13246a 100%)}
.map{left:0;top:2880px;width:1200px;height:300px;background:radial-gradient(ellipse at 50% 60%,rgba(60,90,180,.35),rgba(20,40,110,0) 70%)}
.tabs{left:377px;top:2807px;width:446px;height:71px;display:flex}
.tabs div{display:flex;align-items:center;justify-content:center;font-size:28px;color:var(--white)}
.contact{position:absolute;top:3185px;height:114px;background:#1c2c6c;padding:26px 28px;color:var(--white)}
.contact h4{font-size:18px;font-weight:500;margin-bottom:10px}
.contact p{font-size:14px}
.contact svg{position:absolute;right:18px;top:28px}
.foot-col{position:absolute;top:3352px;color:var(--white)}
.foot-col h5{font-size:18px;font-weight:500;margin-bottom:14px}
.foot-col a{display:block;font-size:14px;color:#8e9bc7;text-decoration:none;line-height:28px}
</style>
</head>
<body>

<div class="abs hero" role="img" aria-label="Photo of a glass balcony railing overlooking a city skyline under a blue sky"></div>

<div class="abs logo" style="left:80px;top:38px">NORVALE</div>
<div class="abs nav" style="left:594px">HOME</div>
<div class="abs nav" style="left:677px">COMPANY</div>
<div class="abs nav" style="left:787px">PRODUCTS</div>
<div class="abs nav" style="left:903px">GALLERY</div>
<div class="btn" style="left:987px;top:43px;width:122px;height:48px;font-size:13px">CONTACT</div>

<div class="abs hero-title">BALUSTER</div>
<div class="abs hero-sub">LEADER IN HOME IMPROVEMENT PRODUCTS</div>
<div class="abs" style="left:1095px;top:290px;width:2px;height:34px;background:var(--navy)"></div>
<div class="abs" style="left:1103px;top:298px;width:1px;height:18px;background:#8a93aa"></div>
<div class="abs" style="left:1110px;top:298px;width:1px;height:18px;background:#8a93aa"></div>
<svg class="abs" style="left:86px;top:558px" width="26" height="22" viewBox="0 0 26 22"><path d="M24 11H3M11 2 2 11l9 9" fill="none" stroke="#0f1e5a" stroke-width="2"/></svg>
<svg class="abs" style="left:138px;top:558px" width="26" height="22" viewBox="0 0 26 22"><path d="M2 11h21M15 2l9 9-9 9" fill="none" stroke="#0f1e5a" stroke-width="2"/></svg>
<div class="btn" style="left:882px;top:530px;width:232px;height:50px;font-size:13px">REVIEW OUR SERVICES
<svg width="16" height="10" viewBox="0 0 16 10"><path d="M1 1l7 7 7-7" fill="none" stroke="#fff" stroke-width="2"/></svg></div>

<!-- services -->
<div class="abs services"></div>
<div class="abs sec-title" style="left:99px;top:671px"><span>OUR SERVICES</span></div>
<div class="abs sec-sub" style="left:99px;top:703px">Featured Solutions</div>

<div class="tile" style="left:99px;top:762px;width:488px;height:191px;background:linear-gradient(135deg,#6b5a48,#9fb2bd 55%,#5d6670)" role="img" aria-label="Glass balcony on a timber-clad building"><div class="tile-label">BALCONIES</div></div>
<div class="tile" style="left:613px;top:762px;width:231px;height:191px;background:linear-gradient(135deg,#d7d9dc,#8b8f95)" role="img" aria-label="Stairs with metal handrail"><div class="tile-label">STAIRS</div></div>
<div class="tile" style="left:870px;top:762px;width:231px;height:191px;background:linear-gradient(135deg,#e6dfd6,#b7a899)" role="img" aria-label="Glass shower enclosure"><div class="tile-label">SHOWER GLASS</div></div>
<div class="tile" style="left:99px;top:982px;width:231px;height:190px;background:linear-gradient(135deg,#c8cbd0,#e9ebee 50%,#a7abb2)" role="img" aria-label="Glass doors in a white wall"><div class="tile-label">GLASS DOORS</div></div>
<div class="tile" style="left:356px;top:982px;width:231px;height:190px;background:linear-gradient(135deg,#5b6128,#9aa62a 50%,#3e3f36)" role="img" aria-label="Green splash back glass in a kitchen"><div class="tile-label">SPLASH BACK GLASS</div></div>
<div class="tile" style="left:613px;top:982px;width:488px;height:190px;background:linear-gradient(90deg,#9aa09f,#cfd4d2 50%,#b3b9b8)" role="img" aria-label="Frosted glass office partitions"><div class="tile-label">OFFICE PARTITIONS</div></div>

<!-- about -->
<div class="abs sec-title" style="left:86px;top:1303px"><span>ABOUT US</span></div>
<div class="abs sec-sub" style="left:86px;top:1334px">Balustrade Importer and Installer</div>
<div class="abs about-text">
<p>Lorem ipsum dolor sit amet, consectetur adipiscing elit, sed do eiusmod tempor incididunt ut labore et dolore magna aliqua. Ut enim ad minim veniam, quis nostrud exercitation ullamco laboris nisi ut aliquip ex ea commodo consequat. Duis aute irure dolor in reprehenderit in voluptate velit esse cillum dolore eu fugiat nulla pariatur. Excepteur sint occaecat cupidatat non proident, sunt in culpa qui officia deserunt mollit anim id est laborum.</p>
<p>Lorem ipsum dolor sit amet, consectetur adipiscing elit, sed do eiusmod tempor incididunt ut labore et dolore magna aliqua.</p>
</div>
<div class="btn" style="left:86px;top:1570px;width:171px;height:49px;font-size:13px">MORE DETAIL
<svg width="16" height="14" viewBox="0 0 16 14"><path d="M1 7h13M9 2l5 5-5 5" fill="none" stroke="#fff" stroke-width="1.8"/></svg></div>
<div class="abs" style="left:789px;top:1305px;width:326px;height:325px;background:linear-gradient(180deg,#1d46b8 0%,#2a4da8 40%,#4b5f88 55%,#8e98a8 72%,#c9ccd2 100%)" role="img" aria-label="Glass balustrade on a terrace with a blurred city at night"></div>

<!-- features -->
<div class="badge" style="left:191px;top:1719px"><div class="core"><svg width="30" height="30" viewBox="0 0 24 24"><path d="M12 2 4 5v6c0 5 3.5 9 8 11 4.5-2 8-6 8-11V5z" fill="none" stroke="#fff" stroke-width="1.8"/><path d="m8.5 12 2.5 2.5 4.5-5" fill="none" stroke="#fff" stroke-width="1.8"/></svg></div></div>
<div class="badge" style="left:543px;top:1719px"><div class="core"><svg width="32" height="28" viewBox="0 0 28 24"><path d="M2 4h15v13H2zM17 9h5l4 4v4h-9z" fill="none" stroke="#fff" stroke-width="1.8"/><circle cx="7" cy="19" r="2.5" fill="#1b3a9c" stroke="#fff" stroke-width="1.8"/><circle cx="21" cy="19" r="2.5" fill="#1b3a9c" stroke="#fff" stroke-width="1.8"/></svg></div></div>
<div class="badge" style="left:894px;top:1719px"><div class="core"><svg width="30" height="30" viewBox="0 0 24 24"><circle cx="12" cy="12" r="9.5" fill="none" stroke="#fff" stroke-width="1.8"/><circle cx="9" cy="10" r="1.2" fill="#fff"/><circle cx="15" cy="10" r="1.2" fill="#fff"/><path d="M8 14.5c2 2.5 6 2.5 8 0" fill="none" stroke="#fff" stroke-width="1.8"/></svg></div></div>

<div class="card" style="left:86px"><h3>HIGH DURABILITY</h3><p>We use the most exclusive and high quality products in railing manufacturing</p></div>
<div class="card" style="left:438px"><h3>FAST DELIVERY</h3><p>Your orders are processed quickly and delivered on the date you requested</p></div>
<div class="card" style="left:789px"><h3>CUSTOMER HAPPINESS</h3><p>Customer satisfaction is our top priority in all our services</p></div>

<!-- projects -->
<div class="abs sec-title" style="left:99px;top:2132px"><span>RECENT PROJECTS</span></div>
<div class="abs sec-sub" style="left:99px;top:2164px">Featured Solutions</div>
<div class="abs" style="left:99px;top:2236px;width:231px;height:174px;background:linear-gradient(135deg,#7a6a55,#c9d1d7 55%,#5a544c)" role="img" aria-label="Glass and steel balcony railings"></div>
<div class="abs" style="left:356px;top:2236px;width:231px;height:174px;background:linear-gradient(135deg,#4a4b4e,#8a8b8e 55%,#d9dadc)" role="img" aria-label="Walk-in glass shower"></div>
<div class="abs" style="left:613px;top:2236px;width:231px;height:174px;background:linear-gradient(135deg,#b8c3c4,#e8ecec 55%,#5a6668)" role="img" aria-label="Glass partitions in an office corridor"></div>
<div class="abs" style="left:870px;top:2236px;width:231px;height:174px;background:linear-gradient(135deg,#d9dbdc,#9aa59a 50%,#3c3b3a)" role="img" aria-label="Glass walled meeting room"></div>
<div class="btn" style="left:906px;top:2439px;width:195px;height:49px;font-size:13px">MORE PROJECTS
<svg width="16" height="14" viewBox="0 0 16 14"><path d="M1 7h13M9 2l5 5-5 5" fill="none" stroke="#fff" stroke-width="1.8"/></svg></div>

<!-- stats -->
<div class="abs stats"></div>
<div class="stat" style="left:152px"><svg width="58" height="58" viewBox="0 0 24 24"><path d="M2 3h20v14H9l-5 5v-5H2z" fill="#0f1e5a"/><path d="m7 10 3.5 3.5L17 7" fill="none" stroke="#fff" stroke-width="2"/></svg><div><b>15.000+</b><small>Completed Service</small></div></div>
<div class="stat" style="left:493px"><svg width="58" height="58" viewBox="0 0 24 24"><path d="M12 2 1 7.5 12 13l11-5.5z" fill="#0f1e5a"/><path d="M3 11l9 4.5 9-4.5M3 15l9 4.5 9-4.5" fill="none" stroke="#0f1e5a" stroke-width="2.4"/></svg><div><b>25+</b><small>Years of Experience</small></div></div>
<div class="stat" style="left:867px"><svg width="72" height="58" viewBox="0 0 30 24"><circle cx="15" cy="7" r="4.5" fill="#0f1e5a"/><circle cx="6" cy="9" r="3" fill="#0f1e5a"/><circle cx="24" cy="9" r="3" fill="#0f1e5a"/><path d="M7 22c0-5 3.5-8 8-8s8 3 8 8z M0 21c0-4 2-6 5-6 1.5 0 2.5.5 3 1-1.5 1.5-2 3-2 5z M30 21c0-4-2-6-5-6-1.5 0-2.5.5-3 1 1.5 1.5 2 3 2 5z" fill="#0f1e5a"/></svg><div><b>15+</b><small>Our Staff</small></div></div>

<!-- worldwide -->
<div class="abs world"></div>
<div class="abs map" role="img" aria-label="Dotted world map with export bars"></div>
<div class="abs tabs"><div style="width:220px;background:#1a3591">5 Continent</div><div style="width:226px;background:#22409f">+40 Country</div></div>
<div class="abs" style="left:0;top:2916px;width:1200px;text-align:center;font-size:42px;font-weight:800;color:var(--white)">NORVALE WORLDWIDE</div>
<div class="abs" style="left:0;top:2992px;width:1200px;text-align:center;font-size:21px;color:var(--white)">COUNTRIES WE EXPORT</div>

<div class="contact" style="left:93px;width:328px"><h4>Support</h4><p>(+90) 512 000 4417</p>
<svg width="58" height="58" viewBox="0 0 24 24" opacity=".25"><path d="M4 14v-2a8 8 0 0 1 16 0v2" fill="none" stroke="#fff" stroke-width="2"/><rect x="3" y="13" width="5" height="7" rx="2" fill="#fff"/><rect x="16" y="13" width="5" height="7" rx="2" fill="#fff"/></svg></div>
<div class="contact" style="left:435px;width:329px"><h4>E-Mail</h4><p>mail@norvale.example</p>
<svg width="58" height="58" viewBox="0 0 24 24" opacity=".25"><path d="M2 10 12 3l10 7v11H2z" fill="#fff"/><path d="m2 10 10 6 10-6" fill="none" stroke="#1c2c6c" stroke-width="1.5"/></svg></div>
<div class="contact" style="left:779px;width:327px"><h4>Address</h4><p>2140 Linden Avenue Westford</p>
<svg width="50" height="58" viewBox="0 0 24 24" opacity=".25"><path d="M12 2a7 7 0 0 0-7 7c0 5 7 13 7 13s7-8 7-13a7 7 0 0 0-7-7z" fill="#fff"/><circle cx="12" cy="9" r="2.5" fill="#1c2c6c"/></svg></div>

<div class="abs logo" style="left:98px;top:3348px;color:var(--white)">NORVALE</div>
<div class="abs" style="left:99px;top:3416px;width:320px;font-size:14px;line-height:21px;color:#8e9bc7">Lorem ipsum dolor sit amet, consectetur adipiscing elit, sed do eiusmod tempor incididunt ut labore et dolore magna aliqua.</div>
<div class="abs" style="left:99px;top:3493px;width:219px;height:42px;background:#1c2c6c;display:flex;align-items:center;justify-content:space-around;padding:0 14px">
<span style="width:10px;height:10px;border-radius:50%;background:#8e9bc7"></span><span style="width:10px;height:10px;border-radius:50%;background:#8e9bc7"></span><span style="width:10px;height:10px;border-radius:50%;background:#8e9bc7"></span><span style="width:10px;height:10px;border-radius:50%;background:#8e9bc7"></span>
</div>
<div class="foot-col" style="left:468px"><h5>Company</h5><a href="#">About</a><a href="#">Our Vision</a><a href="#">Our Mission</a><a href="#">Gallery</a></div>
<div class="foot-col" style="left:811px"><h5>Services</h5><a href="#">Stairs</a><a href="#">Glass Doors</a><a href="#">Shower Glass</a><a href="#">Office Partitions</a></div>

</body>
</html>
```